A sticker for hackers! "I AM OFFENSIVE"

"I AM OFFENSIVE" I need a sticker! Help us hack stuff!

We hack stuff. That is what we do. We are an offensive security company. We need a sticker. This is a sticker that will go on people's laptops. I want the text to say "I am offensive" and have the company logo.

Just think, this sticker will be on the laptops of hundreds of hackers!

I would like a small version of the logo on the sticker.

Target Market(s)

A sticker to go on the laptops of information security people, mostly hackers (the good guys!)

Industry/Entity Type

Computer Security

Requirements
Must have
• The logo. I'm ok with rearranging the logo and the text.
• "I am offensive" must be in the sticker
Nice to have
• Most of the focus should be on the text "I am offensive". Logo/name should be smaller.
Should not have
• Do not change the text
• No font change on the logo

```html
<!DOCTYPE html>
<html lang="en">
<head>
<meta charset="utf-8">
<title>I Am Offensive – Sticker Designs</title>
<link rel="stylesheet" href="https://fonts.googleapis.com/css2?family=Amatic+SC:wght@700&family=Arimo:wght@400&display=swap">
<style>
  :root {
    --paper: #ffffff;
    --outline: #2b2b2b;
    --slogan-blue: #1b75bc;
    --brand-red: #e0232e;
    --brand-ink: #1a1a1a;
    --label-ink: #111111;
  }
  html, body {
    margin: 0;
    padding: 0;
    width: 1200px;
    height: 800px;
    overflow: hidden;
    background: var(--paper);
  }
  .sheet {
    display: block;
    width: 1200px;
    height: 800px;
  }
  .sticker-outline {
    fill: var(--paper);
    stroke: var(--outline);
    stroke-width: 0.9;
  }
  .slogan-rough {
    font-family: "Amatic SC", cursive;
    font-weight: 700;
    font-size: 96px;
    fill: var(--slogan-blue);
  }
  .slogan-clean {
    font-family: "Arimo", Arial, sans-serif;
    font-weight: 400;
    font-size: 65px;
    fill: var(--slogan-blue);
  }
  .brand-mark {
    fill: var(--brand-red);
  }
  .brand-name {
    font-family: "Arimo", Arial, sans-serif;
    font-weight: 400;
    font-size: 22px;
    fill: var(--brand-ink);
  }
  .design-label {
    font-family: "Arimo", Arial, sans-serif;
    font-weight: 400;
    font-size: 25px;
    fill: var(--label-ink);
  }
</style>
</head>
<body>
<svg class="sheet" viewBox="0 0 1200 800" xmlns="http://www.w3.org/2000/svg">
  <!-- Option one: rough display lettering -->
  <g class="sticker sticker--rough">
    <ellipse class="sticker-outline" cx="607" cy="210" rx="309" ry="112"/>
    <text class="slogan-rough" x="356" y="226" textLength="492" lengthAdjust="spacingAndGlyphs">I AM OFFENSIVE</text>
    <rect class="brand-mark" x="659" y="240" width="24" height="34"/>
    <text class="brand-name" x="697" y="265" textLength="153" lengthAdjust="spacing">IRONKEEP</text>
  </g>
  <text class="design-label" x="310" y="339">Design 1</text>

  <!-- Option two: clean sans lettering -->
  <g class="sticker sticker--clean">
    <ellipse class="sticker-outline" cx="623" cy="559" rx="309" ry="112"/>
    <text class="slogan-clean" x="372" y="576" textLength="498" lengthAdjust="spacingAndGlyphs">I AM OFFENSIVE</text>
    <rect class="brand-mark" x="675" y="591" width="24" height="33"/>
    <text class="brand-name" x="712" y="616" textLength="154" lengthAdjust="spacing">IRONKEEP</text>
  </g>
  <text class="design-label" x="310" y="691">Design 2</text>
</svg>
</body>
</html>
```